Business card and letterhead for a healthcare facility.
The Meadow
Cutting-Edge
Bright-And-Fun-filled
Rohan Subramani
Prosthodontist
4382 Copper Creek Parkway, Suite 410. Annandale, Va 22015
dr.s@pmbvirginia.com
www.themeadow714.com

```html
<!DOCTYPE html>
<html lang="en">
<head>
<meta charset="UTF-8">
<title>The Meadow – Business Card</title>
<link rel="stylesheet" href="https://fonts.googleapis.com/css2?family=Montserrat:wght@400;500;600;700&family=Roboto+Slab:wght@600;700&display=swap">
<style>
  :root {
    --navy: #152a4c;
    --gold: #f5b324;
    --white: #ffffff;
    --ink: #1d2d4a;
    --grey: #6b7280;
    --rule: #c9cdd4;
    --backdrop: #e6e7ea;
  }
  * { box-sizing: border-box; margin: 0; padding: 0; }
  html, body { width: 1200px; height: 871px; overflow: hidden; }
  body {
    background: var(--backdrop);
    font-family: "Montserrat", Arial, sans-serif;
    position: relative;
  }
  .card {
    position: absolute;
    left: 250px;
    width: 700px;
    height: 400px;
    overflow: hidden;
    box-shadow: 0 6px 18px rgba(0,0,0,.18);
  }
  .card--front { top: 20px; background: var(--navy); color: var(--white); }
  .card--back { top: 451px; background: var(--white); color: var(--ink); }

  /* Name lockup: invented name plus one plain circle beside it */
  .brand { display: flex; align-items: center; gap: 14px; white-space: nowrap; }
  .brand__dot { border-radius: 50%; background: var(--gold); flex: none; }
  .brand__name { font-weight: 600; line-height: 1; letter-spacing: -0.5px; }

  /* Front */
  .card--front .brand {
    position: absolute; top: 118px; left: 0; right: 0; justify-content: center;
  }
  .card--front .brand__dot { width: 22px; height: 22px; }
  .card--front .brand__name { font-size: 56px; color: var(--white); }
  .appointment {
    position: absolute; top: 248px; left: 0; right: 0; text-align: center;
  }
  .appointment__title {
    font-family: "Roboto Slab", Georgia, serif;
    color: var(--gold); font-weight: 700; font-size: 18px;
  }
  .appointment__fields {
    display: flex; justify-content: center; gap: 24px; margin-top: 28px;
    color: var(--gold); font-size: 13px;
  }
  .appointment__field { display: flex; align-items: flex-end; gap: 8px; }
  .appointment__line { width: 150px; border-bottom: 1px solid var(--gold); height: 1px; margin-bottom: 4px; }

  /* Back */
  .card--back .brand {
    position: absolute; left: 36px; top: 150px; width: 300px; justify-content: center;
  }
  .card--back .brand__dot { width: 16px; height: 16px; }
  .card--back .brand__name { font-size: 42px; color: var(--navy); }
  .divider {
    position: absolute; left: 350px; top: 60px; width: 1px; height: 190px;
    background: var(--rule);
  }
  .contact { position: absolute; left: 372px; top: 62px; }
  .contact__name {
    font-family: "Roboto Slab", Georgia, serif;
    font-weight: 700; font-size: 20px; color: var(--navy); letter-spacing: .5px;
    white-space: nowrap;
  }
  .contact__role { font-size: 13px; color: var(--grey); margin-top: 4px; }
  .contact__address { font-size: 12px; color: var(--grey); line-height: 1.5; margin-top: 24px; }
  .contact__list { list-style: none; margin-top: 20px; }
  .contact__item {
    display: flex; align-items: center; gap: 8px;
    font-size: 12px; color: var(--grey); line-height: 1.75;
  }
  .contact__icon { width: 11px; height: 11px; flex: none; }
  .band { position: absolute; left: 0; bottom: 0; width: 700px; height: 90px; }
</style>
</head>
<body>

  <section class="card card--front" aria-label="Card front">
    <div class="brand">
      <span class="brand__dot"></span>
      <span class="brand__name">The Meadow</span>
    </div>
    <div class="appointment">
      <p class="appointment__title">Next Appointment</p>
      <div class="appointment__fields">
        <span class="appointment__field">Time <span class="appointment__line"></span></span>
        <span class="appointment__field">Date <span class="appointment__line"></span></span>
      </div>
    </div>
  </section>

  <section class="card card--back" aria-label="Card back">
    <div class="brand">
      <span class="brand__dot"></span>
      <span class="brand__name">The Meadow</span>
    </div>
    <span class="divider"></span>
    <div class="contact">
      <p class="contact__name">ROHAN SUBRAMANI</p>
      <p class="contact__role">Prosthodontist</p>
      <p class="contact__address">4382 Copper Creek Parkway,<br>Suite 410. Annandale, Va 22015</p>
      <ul class="contact__list">
        <li class="contact__item">
          <svg class="contact__icon" viewBox="0 0 12 12"><path fill="#f5b324" d="M2.5 1l2 2.3-1 1.4c.8 1.5 1.9 2.6 3.3 3.3l1.4-1 2.3 2-.9 1.8C5.3 10.7 1.3 6.7 1 2z"/></svg>
          703 555 0148
        </li>
        <li class="contact__item">
          <svg class="contact__icon" viewBox="0 0 12 12"><rect x="1" y="2.5" width="10" height="7" rx="1" fill="#f5b324"/><path d="M1.5 3l4.5 3.5L10.5 3" stroke="#fff" fill="none" stroke-width="1"/></svg>
          dr.s@pmbvirginia.com
        </li>
        <li class="contact__item">
          <svg class="contact__icon" viewBox="0 0 12 12"><circle cx="6" cy="6" r="5" fill="#f5b324"/><path d="M1 6h10M6 1c-2 2.7-2 7.3 0 10M6 1c2 2.7 2 7.3 0 10" stroke="#fff" fill="none" stroke-width=".8"/></svg>
          www.themeadow714.com
        </li>
      </ul>
    </div>
    <svg class="band" viewBox="0 0 700 90" preserveAspectRatio="none" aria-hidden="true">
      <polygon points="0,62 700,30 700,90 0,90" fill="#152a4c"/>
      <polygon points="560,36 700,8 700,30 540,38" fill="#f5b324"/>
    </svg>
  </section>

</body>
</html>
```